Business Card Design

New business, starting out small. High end residential/ commercial building company in Sydney Australia's prestigious Eastern suburbs, perfection is our motto and we want our marketing design to reflect that.

Therefore marketing towards high end clients. Looking for design concepts that will portray this image and will appeal to both male and females, prototype has been included- see images. Although we are open to ideas we have included this to give direction.

DARK Navy and white is the colour scheme, as per image provided. Logo ideas welcomed, however design is preferred simple, modern and sophisticated.

This business card will be the template and inspiration for website, t-shirt, banners etc to come so if you want the business, show us your design!

Industry/Entity Type

Marketing

Contact Information for Business Card

Company name: Tallow Ridge Building
Catch phrase: Your vision
Owner/operator: Garreth Pell
Phone: 0468172905
Website: www.tallowridgebuilding.com.au
Licence No 518294K
ABN 72 913 804
Email address
(displayed on back of card):info@tallowridgebuilding.com.au

```html
<!DOCTYPE html>
<html lang="en">
<head>
<meta charset="utf-8">
<title>Tallow Ridge Building – Business Card</title>
<link rel="stylesheet" href="https://fonts.googleapis.com/css2?family=Montserrat:wght@600;700&family=Didact+Gothic&display=swap">
<style>
  :root {
    --navy: #27498a;
    --navy-deep: #1f3d78;
    --white: #ffffff;
    --rule: #8a8f98;
    --text-grey: #6b6f76;
    --backdrop: #e6e7e9;
  }
  * { box-sizing: border-box; margin: 0; padding: 0; }
  html, body { width: 1200px; height: 749px; overflow: hidden; }
  body {
    background: var(--backdrop);
    position: relative;
    font-family: "Didact Gothic", sans-serif;
  }
  .card {
    position: absolute;
    top: 225px;
    width: 520px;
    height: 300px;
    overflow: hidden;
    box-shadow: 0 2px 6px rgba(0,0,0,0.15);
  }

  /* Front */
  .card-front { left: 50px; background: var(--white); }
  .front-header {
    position: absolute; left: 0; top: 0; width: 100%; height: 62px;
    background: var(--navy);
    border-bottom: 4px solid var(--rule);
    display: flex; align-items: center; justify-content: center;
  }
  .company-name {
    font-family: "Montserrat", sans-serif; font-weight: 700;
    color: var(--white); font-size: 25px; letter-spacing: 0.5px;
    text-transform: uppercase;
  }
  .brand-mark {
    position: absolute; left: 0; top: 66px; width: 250px; height: 166px;
    display: flex; align-items: center; justify-content: center; gap: 10px;
  }
  .brand-square { width: 18px; height: 18px; background: var(--navy); }
  .brand-name {
    font-family: "Montserrat", sans-serif; font-weight: 700;
    color: var(--navy); font-size: 22px;
  }
  .divider {
    position: absolute; left: 250px; top: 66px; width: 3px; height: 166px;
    background: var(--rule);
  }
  .contact {
    position: absolute; left: 275px; top: 84px; width: 230px;
  }
  .person-name {
    font-family: "Montserrat", sans-serif; font-weight: 700;
    color: var(--navy); font-size: 19px;
  }
  .person-role { color: var(--text-grey); font-size: 14px; margin-bottom: 12px; }
  .details { display: grid; grid-template-columns: 58px 12px auto; row-gap: 2px; font-size: 15px; }
  .details dt { color: var(--text-grey); }
  .details .sep { color: var(--text-grey); }
  .details dd { color: var(--navy); }
  .front-footer {
    position: absolute; left: 0; bottom: 0; width: 100%; height: 68px;
    background: var(--navy);
    display: flex; align-items: center; justify-content: center;
  }
  .website { color: var(--white); font-size: 19px; letter-spacing: 0.3px; }

  /* Back */
  .card-back {
    left: 630px; background: var(--navy);
    display: flex; flex-direction: column; align-items: center;
  }
  .back-texture {
    position: absolute; left: 160px; top: 130px; width: 360px; height: 170px;
    background: linear-gradient(160deg, rgba(255,255,255,0) 20%, rgba(255,255,255,0.07) 60%, rgba(255,255,255,0.02) 100%);
  }
  .back-mark {
    position: relative; margin-top: 52px;
    display: flex; align-items: center; gap: 10px;
  }
  .back-mark .brand-square { background: var(--white); }
  .back-mark .brand-name { color: var(--white); }
  .back-name {
    position: relative; margin-top: 30px;
    font-family: "Montserrat", sans-serif; font-weight: 700;
    color: var(--white); font-size: 25px; text-transform: uppercase; letter-spacing: 0.5px;
  }
  .email { position: relative; margin-top: 6px; color: var(--white); font-size: 16px; }
</style>
</head>
<body>
  <section class="card card-front">
    <header class="front-header"><h1 class="company-name">Tallow Ridge Building</h1></header>
    <div class="brand-mark">
      <span class="brand-square"></span>
      <span class="brand-name">Tallow Ridge</span>
    </div>
    <div class="divider"></div>
    <div class="contact">
      <p class="person-name">Garreth Pell</p>
      <p class="person-role">President</p>
      <dl class="details">
        <dt>Phone</dt><span class="sep">:</span><dd>0468172905</dd>
        <dt>No</dt><span class="sep">:</span><dd>518294K</dd>
        <dt>ABN</dt><span class="sep">:</span><dd>72 913 804</dd>
      </dl>
    </div>
    <footer class="front-footer"><p class="website">www.tallowridgebuilding.com.au</p></footer>
  </section>

  <section class="card card-back">
    <div class="back-texture" role="img" aria-label="Faint roofline decoration in lighter navy"></div>
    <div class="back-mark">
      <span class="brand-square"></span>
      <span class="brand-name">Tallow Ridge</span>
    </div>
    <p class="back-name">Tallow Ridge Building</p>
    <p class="email">info@tallowridgebuilding.com.au</p>
  </section>
</body>
</html>
```